Postcard For neighbors near worksite

We are a residential interior and exterior painting company. I will be sending post cards out in neighborhoods that we will be currently working in. Basically giving the neighbors a "Neighborhood Notice" that we are in the area and would like to give a Free Estimate to anyone in that neighborhood. I will attach a file of another companies idea that I like. Also, I attached my Logo. Brightcoat Painting & More

Target Market(s)

Neighbors near where we are working

Industry/Entity Type

It Company

Requirements
Must have
• Website: Brightcoatpaint.example
• Number: 555.204.6617

```html
<!DOCTYPE html>
<html lang="en">
<head>
<meta charset="utf-8">
<title>Neighborhood Notice – Brightcoat Painting &amp; More</title>
<link rel="stylesheet" href="https://fonts.googleapis.com/css2?family=Oswald:wght@400;700&family=Archivo:wght@700;800;900&display=swap">
<style>
  :root {
    --red: #e3151b;
    --red-deep: #b50c12;
    --red-dark: #7e070b;
    --black: #111111;
    --white: #ffffff;
    --photo-wall: #8a6a4e;
    --photo-shirt: #e9e6e0;
  }
  * { margin: 0; padding: 0; box-sizing: border-box; }
  html, body { width: 667px; height: 1200px; overflow: hidden; background: var(--white); }
  .postcard {
    position: relative;
    width: 667px;
    height: 1200px;
    overflow: hidden;
    background: radial-gradient(ellipse at 50% 45%, var(--red) 0%, var(--red-deep) 60%, var(--red-dark) 100%);
    font-family: "Archivo", Arial, sans-serif;
  }
  .headline { position: absolute; left: 0; top: 62px; width: 100%; text-align: center; color: var(--white); font-family: "Oswald", "Arial Narrow", sans-serif; }
  .headline-kicker { font-weight: 400; font-size: 82px; line-height: 1; letter-spacing: 1px; }
  .headline-main { font-weight: 700; font-size: 196px; line-height: 1; margin-top: -6px; letter-spacing: -2px; }

  .rule { position: absolute; left: 0; width: 100%; height: 7px; background: var(--black); }
  .rule-top { top: 368px; }
  .rule-bottom { top: 857px; }

  .message-panel { position: absolute; left: 0; top: 375px; width: 100%; height: 482px; background: var(--white); }
  .crew-photo { position: absolute; left: 38px; top: 21px; width: 321px; height: 438px;
    background: linear-gradient(160deg, var(--photo-wall) 0%, #6f5540 55%, var(--photo-shirt) 100%); }
  .message-copy { position: absolute; left: 376px; top: 22px; color: var(--black); }
  .message-lead { font-weight: 800; font-size: 33px; line-height: 46px; }
  .service-list { list-style: none; margin-top: 20px; }
  .service-list li { display: flex; align-items: center; gap: 9px; font-weight: 800; font-size: 20px; height: 46px; }
  .service-list svg { width: 21px; height: 21px; flex: none; }

  .offer { position: absolute; left: 0; top: 864px; width: 100%; height: 151px; text-align: center; color: var(--white); padding-top: 10px; }
  .offer-line { font-weight: 900; font-size: 31px; line-height: 46px; letter-spacing: 0.3px; }
  .offer-url { font-weight: 800; font-size: 24px; line-height: 40px; }

  .contact-bar { position: absolute; left: 0; top: 1015px; width: 100%; height: 126px; background: var(--white); }
  .brand-name { position: absolute; left: 46px; top: 22px; width: 240px; color: var(--red); font-weight: 900; font-size: 30px; line-height: 36px; }
  .call-now { position: absolute; left: 300px; top: 18px; width: 340px; text-align: center; color: var(--red); font-weight: 900; }
  .call-now-label { font-size: 38px; line-height: 48px; }
  .call-now-phone { font-size: 41px; line-height: 50px; }
</style>
</head>
<body>
<main class="postcard">
  <header class="headline">
    <div class="headline-kicker">NEIGHBORHOOD</div>
    <div class="headline-main">NOTICE!</div>
  </header>

  <div class="rule rule-top"></div>

  <section class="message-panel">
    <div class="crew-photo" role="img" aria-label="Smiling painter in a white polo shirt with a crew member on a ladder painting a wall behind him"></div>
    <div class="message-copy">
      <p class="message-lead">We are<br>currently<br>painting<br>a house<br>in your<br>neighborhood!</p>
      <ul class="service-list">
        <li><svg viewBox="0 0 20 20"><circle cx="10" cy="10" r="8" fill="none" stroke="#e3151b" stroke-width="2.4"/><path d="M6 10.3l2.8 2.8L14.2 7.4" fill="none" stroke="#111" stroke-width="2.4" stroke-linecap="round" stroke-linejoin="round"/></svg>Interior Painting</li>
        <li><svg viewBox="0 0 20 20"><circle cx="10" cy="10" r="8" fill="none" stroke="#e3151b" stroke-width="2.4"/><path d="M6 10.3l2.8 2.8L14.2 7.4" fill="none" stroke="#111" stroke-width="2.4" stroke-linecap="round" stroke-linejoin="round"/></svg>Exterior Painting</li>
        <li><svg viewBox="0 0 20 20"><circle cx="10" cy="10" r="8" fill="none" stroke="#e3151b" stroke-width="2.4"/><path d="M6 10.3l2.8 2.8L14.2 7.4" fill="none" stroke="#111" stroke-width="2.4" stroke-linecap="round" stroke-linejoin="round"/></svg>General Repairs</li>
      </ul>
    </div>
  </section>

  <div class="rule rule-bottom"></div>

  <section class="offer">
    <p class="offer-line">CALL FOR A FREE ESTIMATE</p>
    <p class="offer-line">WHILE WE ARE IN THE AREA</p>
    <p class="offer-url">www.brightcoatpaint.example</p>
  </section>

  <footer class="contact-bar">
    <div class="brand-name">Brightcoat Painting &amp; More</div>
    <div class="call-now">
      <div class="call-now-label">CALL NOW:</div>
      <div class="call-now-phone">555.204.6617</div>
    </div>
  </footer>
</main>
</body>
</html>
```